Carton Box Packaging For Motorcycle Brake Shoe - Varonel Brand

Packaging Dimensions: 125mm (H) x 125mm (W) x 31mm (D)
We would like to design a genuine Carton box Packaging for motorcycle Brake Shoe.
This is a critical part of the motorcycle, so we need the packaging to reflect elegant impression.
Varonel, is one of the leading companies for manufacturing Motorcycles, located in Egypt. Our company is offering high-quality products, the best in the local market, with very competitive prices.
We have a limited time to get this project done, So we Highly appreciate receiving your designs ASAP.
Target Market(s)
Economical Motorcycle Buyers
Colors
Designer to choose colors to be used in the design.
Look and feel

```html
<!DOCTYPE html>
<html lang="en">
<head>
<meta charset="utf-8">
<title>Varonel Brake Shoe Packaging</title>
<link rel="stylesheet" href="https://fonts.googleapis.com/css2?family=Audiowide&family=Arimo:wght@400&display=swap">
<style>
  :root {
    --backdrop: #ababab;
    --race-blue: #2f7bea;
    --race-blue-light: #8fbcff;
    --race-red: #e0142a;
    --race-red-light: #ff9aa3;
    --ink: #0c0c0c;
    --plate: #141414;
    --paper: #ececec;
    --silver: #e6e6e6;
    --holo-pink: #e6b6f0;
    --holo-blue: #b9e2f3;
    --holo-cream: #f3eed7;
    --mono-light: #e2e2e2;
    --mono-dark: #3a3a3a;
  }
  * { margin: 0; padding: 0; box-sizing: border-box; }
  html, body { width: 848px; height: 1200px; overflow: hidden; }
  body {
    position: relative;
    background: var(--backdrop);
    font-family: "Audiowide", sans-serif;
  }

  /* Shared brand plate */
  .brand-plate {
    position: absolute;
    display: flex; align-items: center; justify-content: center;
  }
  .brand-plate__body {
    display: flex; align-items: center; gap: 8px;
    background: var(--plate);
    border-radius: 4px;
  }
  .brand-plate__dot { border-radius: 50%; background: var(--silver); flex: none; }
  .brand-plate__name { color: var(--silver); line-height: 1; white-space: nowrap; }

  /* Main carton face */
  .carton-face {
    position: absolute;
    left: 159px; top: 126px;
    width: 505px; height: 505px;
    overflow: hidden;
  }
  .carton-face__artwork {
    position: absolute; inset: 0;
    background: linear-gradient(135deg, var(--race-blue-light) 0%, var(--race-blue) 28%, var(--ink) 42%, var(--paper) 52%, var(--race-red-light) 64%, var(--race-red) 82%, var(--paper) 100%);
  }
  .carton-face .brand-plate { left: 0; right: 0; top: 238px; }
  .carton-face .brand-plate__body { padding: 8px 14px; gap: 10px; }
  .carton-face .brand-plate__dot { width: 22px; height: 22px; }
  .carton-face .brand-plate__name { font-size: 32px; }

  .product-pill {
    position: absolute;
    left: 107px; top: 414px;
    width: 294px; height: 52px;
    border-radius: 26px;
    background: linear-gradient(90deg, var(--race-blue-light), #ffd0d6);
    padding: 5px;
  }
  .product-pill__inner {
    width: 100%; height: 100%;
    border-radius: 21px;
    background: var(--paper);
    display: flex; align-items: center; justify-content: center;
    font-size: 30px;
    color: var(--ink);
  }

  /* Sleeve bag */
  .sleeve {
    position: absolute;
    left: 89px; top: 732px;
    width: 252px; height: 347px;
    overflow: hidden;
  }
  .sleeve__header { height: 57px; background: var(--ink); position: relative; }
  .sleeve__notes {
    position: absolute;
    left: 15px; top: 13px;
    width: 74px;
    font-family: "Arimo", sans-serif;
    font-size: 3.4px;
    line-height: 4.3px;
    color: #f2f2f2;
    text-align: justify;
  }
  .sleeve__hang-slot {
    position: absolute;
    left: 124px; top: 20px;
    width: 7px; height: 19px;
    border-radius: 4px;
    background: var(--paper);
  }
  .sleeve__header .brand-plate { right: 10px; top: 22px; }
  .sleeve__header .brand-plate__body { padding: 3px 4px; gap: 3px; background: #2a2a2a; }
  .sleeve__header .brand-plate__dot { width: 7px; height: 7px; }
  .sleeve__header .brand-plate__name { font-size: 8px; }

  .sleeve__window {
    position: absolute;
    left: 0; top: 57px; right: 0; bottom: 0;
    background: linear-gradient(135deg, var(--mono-light) 0%, var(--mono-dark) 40%, var(--mono-light) 60%, var(--mono-dark) 100%);
  }
  .sleeve .sleeve__brand { left: 0; right: 0; top: 236px; }
  .sleeve .sleeve__brand .brand-plate__body { padding: 5px 9px; gap: 6px; background: #2b2b2b; }
  .sleeve .sleeve__brand .brand-plate__dot { width: 14px; height: 14px; background: #d2d2d2; }
  .sleeve .sleeve__brand .brand-plate__name { font-size: 20px; color: #d2d2d2; }

  /* Regulator box */
  .regulator-box {
    position: absolute;
    left: 443px; top: 746px;
    width: 292px; height: 320px;
  }
  .regulator-box__panels { position: absolute; inset: 0; }
  .regulator-box__top-brand { left: 0; width: 290px; top: 15px; }
  .regulator-box__top-brand .brand-plate__body { padding: 2px 5px; gap: 3px; background: #262626; }
  .regulator-box__top-brand .brand-plate__dot { width: 7px; height: 7px; }
  .regulator-box__top-brand .brand-plate__name { font-size: 8px; }

  .regulator-box__front {
    position: absolute;
    left: 0; top: 38px;
    width: 241px; height: 282px;
    overflow: hidden;
  }
  .regulator-box__artwork {
    position: absolute; inset: 0;
    background: linear-gradient(150deg, var(--ink) 0%, var(--holo-pink) 30%, var(--holo-blue) 50%, var(--holo-cream) 68%, var(--ink) 85%, #2a2a2a 100%);
  }
  .regulator-box__front .brand-plate { left: 0; right: 0; top: 132px; }
  .regulator-box__front .brand-plate__body { padding: 5px 9px; gap: 6px; }
  .regulator-box__front .brand-plate__dot { width: 14px; height: 14px; }
  .regulator-box__front .brand-plate__name { font-size: 20px; }
  .regulator-box__label {
    position: absolute;
    left: 0; right: 0; top: 224px;
    text-align: center;
    font-size: 18px;
    color: var(--ink);
  }

  .regulator-box__side-label {
    position: absolute;
    left: 216px; top: 102px;
    width: 104px;
    text-align: center;
    font-size: 12px;
    color: var(--ink);
    transform: rotate(-90deg);
  }
  .regulator-box__side-brand { left: 222px; width: 92px; top: 236px; transform: rotate(-80deg); }
  .regulator-box__side-brand .brand-plate__body { padding: 2px 4px; gap: 3px; }
  .regulator-box__side-brand .brand-plate__dot { width: 6px; height: 6px; }
  .regulator-box__side-brand .brand-plate__name { font-size: 8px; }
</style>
</head>
<body>

<section class="carton-face" aria-label="Brake shoe carton front">
  <div class="carton-face__artwork" role="img" aria-label="Waving chequered racing flag in blue, black, white and red"></div>
  <div class="brand-plate">
    <div class="brand-plate__body">
      <span class="brand-plate__dot"></span>
      <span class="brand-plate__name">Varonel</span>
    </div>
  </div>
  <div class="product-pill">
    <div class="product-pill__inner">break shoe</div>
  </div>
</section>

<section class="sleeve" aria-label="Cable sleeve bag front">
  <div class="sleeve__header">
    <p class="sleeve__notes">Genuine brake parts for daily riders. Fit by a trained mechanic only. Check the lining before each long trip and replace worn shoes in pairs. Keep dry and away from oil. Made for steady stopping power on city and country roads, season after season.</p>
    <span class="sleeve__hang-slot"></span>
    <div class="brand-plate">
      <div class="brand-plate__body">
        <span class="brand-plate__dot"></span>
        <span class="brand-plate__name">Varonel</span>
      </div>
    </div>
  </div>
  <div class="sleeve__window" role="img" aria-label="Black and white chequered flag with a coiled cable visible through clear film"></div>
  <div class="brand-plate sleeve__brand">
    <div class="brand-plate__body">
      <span class="brand-plate__dot"></span>
      <span class="brand-plate__name">Varonel</span>
    </div>
  </div>
</section>

<section class="regulator-box" aria-label="Regulator box">
  <svg class="regulator-box__panels" width="292" height="320" viewBox="0 0 292 320" aria-hidden="true">
    <defs>
      <linearGradient id="side-foil" x1="0" y1="0" x2="0.4" y2="1">
        <stop offset="0" stop-color="#e6b6f0"/>
        <stop offset="0.35" stop-color="#b9e2f3"/>
        <stop offset="0.6" stop-color="#3a3a3a"/>
        <stop offset="0.8" stop-color="#d9c9ec"/>
        <stop offset="1" stop-color="#1c1c1c"/>
      </linearGradient>
    </defs>
    <polygon class="regulator-box__top" points="0,38 47,0 292,0 241,38" fill="#121212"/>
    <polygon class="regulator-box__side" points="241,38 292,0 292,278 241,320" fill="url(#side-foil)"/>
  </svg>
  <div class="brand-plate regulator-box__top-brand">
    <div class="brand-plate__body">
      <span class="brand-plate__dot"></span>
      <span class="brand-plate__name">Varonel</span>
    </div>
  </div>
  <div class="regulator-box__front">
    <div class="regulator-box__artwork" role="img" aria-label="Black chequered flag over holographic pink, blue and cream foil"></div>
    <div class="brand-plate">
      <div class="brand-plate__body">
        <span class="brand-plate__dot"></span>
        <span class="brand-plate__name">Varonel</span>
      </div>
    </div>
    <p class="regulator-box__label">regulator</p>
  </div>
  <p class="regulator-box__side-label">regulator</p>
  <div class="brand-plate regulator-box__side-brand">
    <div class="brand-plate__body">
      <span class="brand-plate__dot"></span>
      <span class="brand-plate__name">Varonel</span>
    </div>
  </div>
</section>

</body>
</html>
```